Ardenwell Building and Property Services needs a business card design

We need a business card design for our building and property services business. We already have a logo we just need a creative design and layout on a business card. Emphasis on clean, modern, professional.
Our client targets are mainly body corporates, building managers, construction managers.
We are a building services company that lean more to structural repair of buildings, through concrete rectification and carbon fibre strengthening.
We also refurbish facades, rendering, painting etc
We target higher end body corporates in prestigious locations, hence why we'd like our cards to reflect professionalism, strength, efficiency

Target Market(s)

body corporates, building managers, construction managers

Industry/Entity Type

Construction

Contact Information for Business Card

Ardenwell is the main word, with 'Building and Property Services' underneath.
Level 17, 82 Harlow Street
MERRIDALE
Melbourne
Vic 3094
T: 9518 2736
Duncan Ferris - Director
dunardenwell@mailbox-example.com

Requirements
Must have
• Stand out on the back of the card- strong/ bold, company logo
• All of the contact details written above
Should not have
• I'd like the card to stand out, especially on the back. Id like the company logo to be prominent, although feel free to be creative around it. But remain clean and professional

```html
<!DOCTYPE html>
<html lang="en">
<head>
<meta charset="utf-8">
<title>Ardenwell Building and Property Services – Business Card</title>
<link href="https://fonts.googleapis.com/css2?family=Cinzel:wght@400;600&family=Lato:wght@400;700&display=swap" rel="stylesheet">
<style>
  :root {
    --stage: #2a2a2a;
    --card-white: #ffffff;
    --band-grey: #5e5e60;
    --band-grey-light: #8a8a8c;
    --brand-blue: #2f86c8;
    --brand-blue-dark: #1f6aa6;
    --text-grey: #6b6b6d;
    --back-dark: #3c3c3e;
    --back-mid: #58585a;
    --line-light: #e4e4e4;
  }
  * { box-sizing: border-box; margin: 0; padding: 0; }
  html, body { width: 1200px; height: 900px; overflow: hidden; }
  body { background: var(--stage); position: relative; font-family: "Lato", sans-serif; }

  .card {
    position: absolute;
    width: 540px;
    height: 330px;
    overflow: hidden;
    box-shadow: 0 10px 30px rgba(0,0,0,.45);
  }

  /* Front */
  .card-front { left: 60px; top: 110px; background: var(--card-white); }
  .name-band {
    position: absolute; left: 0; top: 70px; width: 100%; height: 56px;
    background: linear-gradient(90deg, var(--band-grey) 0%, var(--band-grey) 60%, var(--band-grey-light) 100%);
    border-top: 2px solid var(--brand-blue);
    border-bottom: 2px solid var(--brand-blue);
    outline: 4px solid var(--card-white);
  }
  .name-band::before {
    content: ""; position: absolute; left: 0; top: 16px;
    border-left: 10px solid var(--brand-blue);
    border-top: 10px solid transparent; border-bottom: 10px solid transparent;
  }
  .holder-name {
    position: absolute; left: 32px; top: 13px;
    color: #fff; font-size: 22px; font-weight: 400;
  }
  .holder-role {
    font-size: 13px; letter-spacing: .5px; text-transform: uppercase;
    border-left: 1.5px solid #fff; padding-left: 6px; margin-left: 6px;
  }
  .brand-mark {
    position: absolute; right: 26px; top: 14px;
    font-family: "Cinzel", serif; font-weight: 600; font-size: 22px;
    color: #fff; letter-spacing: 1px;
  }
  .contact-list {
    position: absolute; left: 40px; top: 160px;
    list-style: none; color: var(--text-grey); font-size: 15px;
  }
  .contact-list li { display: flex; align-items: center; gap: 8px; line-height: 21px; }
  .contact-list li.address { align-items: flex-start; margin-top: 20px; }
  .contact-list svg { flex: none; width: 15px; height: 15px; }
  .contact-list li.address svg { margin-top: 3px; }
  .tagline-front {
    position: absolute; right: 34px; bottom: 58px; text-align: right;
    font-family: "Cinzel", serif; font-size: 16px; color: var(--text-grey); line-height: 20px;
  }

  /* Back */
  .card-back {
    left: 600px; top: 450px;
    background: linear-gradient(150deg, var(--back-dark) 0%, var(--back-mid) 55%, var(--back-dark) 100%);
  }
  .back-band {
    position: absolute; left: 0; bottom: 0; width: 100%; height: 44px;
    background: var(--brand-blue);
    border-top: 3px solid var(--line-light);
    box-shadow: 0 -5px 0 var(--back-dark);
  }
  .back-lockup { position: absolute; left: 0; top: 110px; width: 100%; text-align: center; }
  .back-name {
    font-family: "Cinzel", serif; font-weight: 600; font-size: 52px;
    color: var(--brand-blue); letter-spacing: 3px; line-height: 1;
  }
  .back-tagline {
    margin-top: 8px; font-family: "Cinzel", serif; font-size: 12px;
    color: #b9b9bb; letter-spacing: 2px; text-transform: uppercase;
  }
</style>
</head>
<body>

<section class="card card-front" aria-label="Business card front">
  <div class="name-band">
    <p class="holder-name">Duncan Ferris<span class="holder-role">Director</span></p>
    <p class="brand-mark">Ardenwell</p>
  </div>

  <ul class="contact-list">
    <li>
      <svg viewBox="0 0 16 16" aria-hidden="true"><circle cx="8" cy="8" r="8" fill="#2f86c8"/><path d="M5 4.5l1.6-.4.9 2-1 .8a5 5 0 0 0 2.6 2.6l.8-1 2 .9-.4 1.6c-3.6.2-6.7-2.9-6.5-6.5z" fill="#fff"/></svg>
      <span>9518 2736</span>
    </li>
    <li>
      <svg viewBox="0 0 16 16" aria-hidden="true"><circle cx="8" cy="8" r="8" fill="#2f86c8"/><rect x="5.5" y="3.8" width="5" height="3" fill="#fff"/><rect x="4" y="7" width="8" height="3.6" rx=".6" fill="#fff"/><rect x="5.5" y="9.5" width="5" height="2.8" fill="#fff" stroke="#2f86c8" stroke-width=".6"/></svg>
      <span>9518 2736</span>
    </li>
    <li>
      <svg viewBox="0 0 16 16" aria-hidden="true"><circle cx="8" cy="8" r="8" fill="#2f86c8"/><rect x="4" y="5.2" width="8" height="5.6" fill="#fff"/><path d="M4 5.2l4 3 4-3" fill="none" stroke="#2f86c8" stroke-width=".9"/></svg>
      <span>dunardenwell@mailbox-example.com</span>
    </li>
    <li class="address">
      <svg viewBox="0 0 16 16" aria-hidden="true"><path d="M8 .5a6 6 0 0 1 6 6c0 4.2-6 9-6 9s-6-4.8-6-9a6 6 0 0 1 6-6z" fill="#2f86c8"/><circle cx="8" cy="6.5" r="2.3" fill="#fff"/></svg>
      <span>Level 17, 82 Harlow Street<br>MERRIDALE<br>Melbourne, Vic 3094</span>
    </li>
  </ul>

  <p class="tagline-front">Building<br>and Property Services</p>
</section>

<section class="card card-back" aria-label="Business card back">
  <div class="back-lockup">
    <p class="back-name">ARDENWELL</p>
    <p class="back-tagline">Building and Property Services</p>
  </div>
  <div class="back-band"></div>
</section>

</body>
</html>
```